KRT Design Business Card

I need to develop a business card for my real estate design and investment company. Something clean, classic and professional with a modern vibe.

Industry/Entity Type

Real Estate

Font styles to use
Serif
Sans Serif

```html
<!DOCTYPE html>
<html lang="en">
<head>
<meta charset="utf-8">
<title>KRT Design Business Card</title>
<link href="https://fonts.googleapis.com/css2?family=Mulish:wght@400;700&family=Questrial&display=swap" rel="stylesheet">
<style>
  :root {
    --page-bg: #e6e6e6;
    --card-dark: #2a2528;
    --card-light: #ffffff;
    --ink: #3a3a3a;
    --ink-soft: #555555;
    --rule: #6a6a6a;
    --logo-light: #f2f2f2;
  }
  * { margin: 0; padding: 0; box-sizing: border-box; }
  html, body {
    width: 1200px; height: 900px; overflow: hidden;
    background: var(--page-bg);
  }
  .sheet {
    position: relative; width: 1200px; height: 900px;
    display: flex; flex-direction: column; align-items: center; justify-content: center;
    gap: 40px;
  }
  .card {
    position: relative; width: 700px; height: 400px; border-radius: 30px;
    overflow: hidden;
    box-shadow: 0 6px 18px rgba(0,0,0,0.18);
  }
  /* Back side */
  .card-back { background: var(--card-dark); }
  .card-back .pattern-field {
    position: absolute; inset: 0;
    background: linear-gradient(135deg, #2d282b 0%, #252124 100%);
  }
  .card-back .brand {
    position: absolute; left: 0; right: 0; top: 50%; transform: translateY(-50%);
    text-align: center;
    font-family: "Questrial", sans-serif; font-weight: 400;
    font-size: 54px; letter-spacing: 6px; color: var(--logo-light);
  }
  /* Front side */
  .card-front { background: var(--card-light); color: var(--ink); }
  .card-front .brand {
    position: absolute; right: 40px; top: 44px;
    font-family: "Questrial", sans-serif; font-weight: 400;
    font-size: 38px; letter-spacing: 4px; color: var(--ink-soft);
  }
  .holder {
    position: absolute; left: 40px; top: 222px;
    font-family: "Mulish", sans-serif;
  }
  .holder-name { font-weight: 700; font-size: 21px; color: var(--ink); }
  .holder-title {
    font-size: 13px; letter-spacing: 1px; text-transform: uppercase;
    color: var(--ink-soft); margin-top: 2px;
  }
  .divider {
    position: absolute; left: 232px; right: 36px; top: 258px;
    height: 1px; background: var(--rule);
  }
  .contact-list {
    position: absolute; left: 40px; top: 290px; list-style: none;
    font-family: "Questrial", sans-serif; font-size: 20px; color: var(--ink);
  }
  .contact-list li { display: flex; align-items: center; gap: 12px; height: 30px; }
  .contact-list svg { width: 16px; height: 16px; fill: var(--ink); flex: none; }
  .office {
    position: absolute; right: 40px; top: 274px; text-align: right;
    font-family: "Questrial", sans-serif; font-size: 18px; line-height: 26px;
    color: var(--ink-soft);
  }
</style>
</head>
<body>
<main class="sheet">
  <section class="card card-back">
    <div class="pattern-field" role="img" aria-label="Dark background with a subtle pattern of thin grey chevron lines"></div>
    <div class="brand">KRT Design</div>
  </section>

  <section class="card card-front">
    <div class="brand">KRT Design</div>

    <div class="holder">
      <div class="holder-name">Daniel Marsh</div>
      <div class="holder-title">Managing Director</div>
    </div>
    <div class="divider"></div>

    <ul class="contact-list">
      <li>
        <svg viewBox="0 0 16 16" aria-hidden="true"><path d="M4 0h8a1.5 1.5 0 0 1 1.5 1.5v13A1.5 1.5 0 0 1 12 16H4a1.5 1.5 0 0 1-1.5-1.5v-13A1.5 1.5 0 0 1 4 0zm0.5 2v10h7V2zM8 13a1 1 0 1 0 0 2a1 1 0 0 0 0-2z"/></svg>
        <span>555 214 30 17</span>
      </li>
      <li>
        <svg viewBox="0 0 16 16" aria-hidden="true"><path d="M4 1h8v4H4zM1 6h14v6h-3v3H4v-3H1zm4 4v4h6v-4z"/></svg>
        <span>555 214 30 18</span>
      </li>
      <li>
        <svg viewBox="0 0 16 16" aria-hidden="true"><path d="M0 3h16v1.2L8 9 0 4.2zM0 6l8 4.8L16 6v7H0z"/></svg>
        <span>dmarsh@krtdesign.com</span>
      </li>
    </ul>

    <address class="office" style="font-style:normal">
      48 Harbor Lane<br>
      Millbrook, New York 12545<br>
      www.krtdesign.com
    </address>
  </section>
</main>
</body>
</html>
```